The Velvet Groove Company Brochure

I am the owner of a Mobile Disc Jockey company specializing in weddings. I am looking for a Tri Fold color brochure that is modern and eye catching with the focus being on upscale wedding events. I also want it to be easy to read and not overly cluttered ! I would like it to reflect our website located at thevelvetgroovehq.com
I also have different variations and file types of my logo such as jpeg and png files. I need some good dance floor pics. If you do not have any good stock photos I can look through my photo library. I uploaded a logo and pic I found from one of my videos. Not sure if it is worth anything.
We also do Uplighting and Photo Booths which I would like in the brochure. Much of the text copy needed can be taken from our website if needed. Please refer to the website to see what we do and our style.

Target Market(s)

upscale weddings

Industry/Entity Type

wedding dj entertainment & masters of ceremonies

Requirements
Nice to have
• nice pictures of packed dance floors and people having fun

```html
<!DOCTYPE html>
<html lang="en">
<head>
<meta charset="utf-8">
<title>The Velvet Groove – Tri-Fold Brochure</title>
<link href="https://fonts.googleapis.com/css2?family=Montserrat:wght@400;600;700&family=Great+Vibes&family=Libre+Baskerville&display=swap" rel="stylesheet">
<style>
:root{
  --purple:#5b1f6e;
  --purple-deep:#3a0f4c;
  --magenta:#a51fb2;
  --lavender:#c7a2e0;
  --orange:#f0913f;
  --red:#de3b52;
  --paper:#f2f2f3;
  --ink:#3b3b3f;
  --gray-logo:#6d6d72;
}
*{box-sizing:border-box;margin:0;padding:0}
html,body{width:900px;height:1200px;overflow:hidden;background:#fff}
body{position:relative;font-family:"Montserrat",sans-serif;color:var(--ink)}
.abs{position:absolute}
.sheet{position:absolute;overflow:hidden;background:linear-gradient(90deg,var(--paper),#fff 50%,var(--paper));box-shadow:0 2px 6px rgba(0,0,0,.25)}
.sheet-front{left:30px;top:30px;width:707px;height:550px}
.sheet-inside{left:123px;top:597px;width:750px;height:583px}
.side-label{position:absolute;font-family:"Libre Baskerville",serif;font-size:50px;letter-spacing:2px;color:#111;transform:rotate(-90deg);transform-origin:center}
.label-front{left:700px;top:330px;width:180px;text-align:center}
.label-inside{left:-10px;top:912px;width:190px;text-align:center}
.photo{position:absolute}
.photo-party{background:linear-gradient(135deg,#6a4a3a,#c9a38a 45%,#3a2a2a)}
.photo-purple{background:linear-gradient(135deg,#2a0f35,#8a2c8f 55%,#3a1440)}
.photo-warm{background:linear-gradient(135deg,#4b2a1f,#b67b5a 50%,#e5c9a8)}
.photo-soft{background:linear-gradient(135deg,#b8a8c8,#efe7f2 55%,#8f7aa3)}
.photo-outdoor{background:linear-gradient(135deg,#6a8b6a,#d9d3c5 50%,#8e7c6a)}
.circle{border-radius:50%;border:4px solid #fff;box-shadow:0 0 0 3px var(--lavender)}
.bar-label{position:absolute;left:0;background:var(--purple);color:#fff;font-weight:700;font-size:8.5px;padding:0 16px;display:flex;flex-direction:column;justify-content:center;line-height:11px;white-space:nowrap}
.bar-label .hi{color:var(--orange)}
.box-label{position:absolute;left:0;background:var(--red);color:#fff;font-weight:600;font-size:9.5px;letter-spacing:.3px;padding:0 16px;display:flex;align-items:center;white-space:nowrap}
.tagline{color:var(--purple);font-size:7.5px;line-height:11px}
.body-copy{position:absolute;font-size:6.4px;line-height:9.6px;color:var(--ink)}
.body-copy p+p{margin-top:9px}
.rule{position:absolute;height:1px;background:var(--red);width:100px}
.rule-gray{background:#999}
.contact{position:absolute;font-size:7.5px;line-height:12px;color:var(--ink)}
.contact .row{display:flex;align-items:center;gap:5px}
.contact svg{width:7px;height:7px;fill:var(--purple)}
.brand-name{font-weight:600;color:var(--gray-logo);display:flex;align-items:center;gap:6px;white-space:nowrap}
.brand-dot{display:inline-block;border-radius:50%;background:var(--purple)}
.script{font-family:"Great Vibes",cursive;color:#fff;font-size:30px}
.serif-caps{font-family:"Libre Baskerville",serif;color:#fff;font-size:10.5px;letter-spacing:.5px;line-height:14px;text-transform:uppercase}
.service-title{position:absolute;font-weight:700;font-size:9.5px;color:var(--purple)}
.service-copy{position:absolute;font-size:6.4px;line-height:9.4px;color:var(--ink)}
</style>
</head>
<body>

<section class="sheet sheet-front" aria-label="Brochure front">
  <div class="photo photo-party" style="left:238px;top:0;width:469px;height:300px" role="img" aria-label="Photo of a bride and groom dancing under falling confetti"></div>

  <svg class="abs" style="left:0;top:0" width="707" height="550" viewBox="0 0 707 550" aria-hidden="true">
    <path d="M238 300 C330 250 500 215 707 212 L707 550 L238 550 Z" fill="#ededf0"/>
    <path d="M250 292 C350 230 520 205 707 212 L707 455 C620 475 540 470 470 498 L470 300 C400 280 320 285 250 292 Z" fill="var(--purple)"/>
    <path d="M238 60 C300 120 260 220 300 270" stroke="var(--purple)" stroke-width="22" fill="none"/>
    <path d="M260 300 C360 245 520 222 707 226" stroke="var(--lavender)" stroke-width="6" fill="none"/>
    <path d="M250 120 C330 200 300 260 420 240 C520 220 600 160 707 140" stroke="var(--orange)" stroke-width="1" fill="none"/>
    <path d="M470 470 C560 455 640 440 707 420" stroke="var(--orange)" stroke-width="1" fill="none"/>
    <path d="M470 500 C560 470 640 465 707 462" stroke="var(--lavender)" stroke-width="5" fill="none"/>
  </svg>

  <div class="abs" style="left:0;top:0;width:238px;height:550px;background:linear-gradient(90deg,#e9e9eb,#fafafa)"></div>
  <div class="bar-label" style="top:25px;width:207px;height:26px">
    <span><span class="hi">PACKING</span> DANCE FLOORS SINCE 1981!</span>
  </div>
  <p class="abs tagline" style="left:16px;top:62px;width:185px">Modern – Elegant – Attention to Detail – Personalized – Fun</p>
  <div class="body-copy" style="left:16px;top:96px;width:212px">
    <p>The Velvet Groove is a professional wedding DJ, lighting and photobooth company operating out of Estero, Florida and serving the Naples, Fort Myers, Captiva, Marco &amp; Sanibel Islands and surrounding areas. We bring a wealth of expertise, fun and knowledge to every celebration and constantly exceed our client's expectations. Our talented team of DJs and MCs are passionate about making your event an unforgettable party.</p>
    <p>We know how much work goes into planning a wedding or the simplest event so we've created a simple process to make planning your wedding or event easy, fun and stress free! For weddings everything from your ceremony to the end of your reception will be crafted your way for an experience your guests will be talking about for years to come.</p>
  </div>
  <div class="rule" style="left:16px;top:234px"></div>
  <div class="bar-label" style="top:262px;width:207px;height:30px">
    <span>THE <span class="hi">MOST RECOMMENDED</span> DJ'S</span>
    <span>IN SOUTHWEST FLORIDA</span>
  </div>
  <div class="body-copy" style="left:16px;top:305px;width:212px">
    <p>Our award winning Djs are recommended by the finest venues in Naples, Fort Myers and the surrounding areas and we are known for helping our clients create the ultimate wedding entertainment experience.</p>
    <p>We offer creative ideas and a fresh approach to help you customize your event around the style &amp; vibe that you want. Planning this way is fun and eliminates the stress that comes with preparing for your special day.</p>
    <p>Are Packed dance floors, personalization, and lots of tired people smiling on their way out at the end of the night how you want your wedding to be remembered? If so, then contact us.</p>
  </div>
  <div class="rule rule-gray" style="left:16px;top:433px"></div>
  <div class="photo photo-purple" style="left:0;top:442px;width:238px;height:108px" role="img" aria-label="Photo of guests dancing on a crowded dance floor"></div>

  <div class="photo photo-warm circle" style="left:266px;top:240px;width:122px;height:122px" role="img" aria-label="Photo of a DJ mixing console with warm bokeh lights"></div>
  <div class="brand-name abs" style="left:322px;top:430px;font-size:8px">
    <span class="brand-dot" style="width:8px;height:8px"></span>The Velvet Groove
  </div>
  <div class="contact" style="left:316px;top:462px">
    <div class="row"><span style="width:7px"></span>The Velvet Groove</div>
    <div class="row"><span style="width:7px"></span>Palm Harbor, FL 34600</div>
    <div class="row" style="margin-top:5px"><svg viewBox="0 0 10 10"><path d="M2 0h2l1 3-1.5 1a6 6 0 0 0 2.5 2.5L7 5l3 1v2a2 2 0 0 1-2 2A8 8 0 0 1 0 2a2 2 0 0 1 2-2z"/></svg>555.014.2290</div>
    <div class="row"><svg viewBox="0 0 10 10"><path d="M0 2h10v6H0zM0 2l5 3.5L10 2" stroke="#fff" stroke-width=".8"/></svg>hello@thevelvetgroovehq.com</div>
    <div class="row"><svg viewBox="0 0 10 10"><circle cx="5" cy="5" r="4.5"/></svg>www.thevelvetgroovehq.com</div>
  </div>

  <p class="abs script" style="left:495px;top:270px">It's your day.</p>
  <p class="abs serif-caps" style="left:505px;top:314px;width:190px;text-align:center">Let us help you make<br>it happen, your way</p>
  <div class="photo photo-soft circle" style="left:545px;top:365px;width:92px;height:92px" role="img" aria-label="Photo of a bride and groom sharing a first dance"></div>
  <div class="brand-name abs" style="left:480px;top:492px;font-size:18px">
    <span class="brand-dot" style="width:16px;height:16px"></span>The Velvet Groove
  </div>
</section>
<div class="side-label label-front">FRONT</div>

<section class="sheet sheet-inside" aria-label="Brochure inside">
  <div class="photo photo-purple" style="left:247px;top:0;width:503px;height:215px" role="img" aria-label="Photo of wedding guests dancing with raised arms under purple uplighting"></div>
  <svg class="abs" style="left:0;top:0" width="750" height="583" viewBox="0 0 750 583" aria-hidden="true">
    <path d="M247 28 C330 100 400 185 480 200 C600 218 690 192 750 168 L750 240 L247 240 Z" fill="#f2f2f3"/>
    <path d="M0 0 L150 0 C210 4 250 14 285 34 C360 90 410 168 490 184 C600 204 690 178 750 150 L750 182 C680 212 600 224 480 210 C400 196 340 132 275 58 C225 22 160 10 0 10 Z" fill="var(--purple-deep)"/>
    <path d="M0 3 C150 3 220 12 280 38 C350 84 390 140 430 168" stroke="var(--magenta)" stroke-width="5" fill="none"/>
    <path d="M480 206 C600 218 680 195 750 172" stroke="var(--magenta)" stroke-width="5" fill="none"/>
    <path d="M0 16 C170 18 250 40 300 80 C380 150 420 205 500 220 C610 236 700 210 750 198" stroke="var(--orange)" stroke-width="1" fill="none"/>
  </svg>

  <div class="box-label" style="top:20px;height:30px;width:98px">ABOUT US</div>
  <div class="body-copy" style="left:16px;top:62px;width:220px">
    <p>With over 30+ years of experience providing DJ entertainment and lighting services for corporate events and company parties, we understand how important creating the right atmosphere and delivering quality entertainment is to the success of your event.</p>
    <p>Beginning with your initial consultation, we listen to you and respond with creative ideas and helpful advice so your event is all about you. We know it's more than just great music, it's keeping you guests engaged and coordinating with your venue and vendors for a smooth and timely event everyone will never forget.</p>
  </div>
  <div class="rule rule-gray" style="left:16px;top:183px"></div>
  <div class="box-label" style="top:203px;height:30px;width:145px">SERVICES WE OFFER</div>

  <div class="photo photo-outdoor" style="left:0;top:251px;width:247px;height:100px" role="img" aria-label="Photo of a wedding couple celebrating with guests outdoors"></div>
  <p class="service-title" style="left:16px;top:360px">1. Wedding Ceremonies</p>
  <p class="service-copy" style="left:16px;top:375px;width:220px">We will be happy to provide your ceremony sound system, music and help you with the planning and organizational flow of your ceremony.</p>

  <div class="photo photo-purple" style="left:0;top:420px;width:247px;height:97px" role="img" aria-label="Photo of a couple dancing on a low cloud of fog"></div>
  <p class="service-title" style="left:16px;top:527px">2. Dancing on Clouds</p>
  <p class="service-copy" style="left:16px;top:542px;width:220px">Want to add that fairy tale romance that will "wow" your guests. Add our dancing on clouds option.</p>

  <div class="photo photo-warm" style="left:255px;top:215px;width:237px;height:106px" role="img" aria-label="Photo of a reception hall with uplighting and centerpieces"></div>
  <p class="service-title" style="left:262px;top:328px">3. Lighting</p>
  <p class="service-copy" style="left:262px;top:343px;width:225px">Uplighting can transform the atmosphere in your room from ordinary to extraordinary! When used with dance floor lighting it creates both energy and atmosphere.</p>

  <div class="photo photo-soft" style="left:255px;top:396px;width:237px;height:100px" role="img" aria-label="Photo of a monogram projected on a draped wall"></div>
  <p class="service-title" style="left:262px;top:506px">4. Monogram Lighting</p>
  <p class="service-copy" style="left:262px;top:521px;width:225px">Add more style! Let us put your name in lights. We offer over 20 different designs for you to choose from or we can create a custom design for you.</p>

  <div class="photo photo-party" style="left:505px;top:221px;width:230px;height:100px" role="img" aria-label="Photo of guests posing with photo booth props"></div>
  <p class="service-title" style="left:510px;top:330px">5. Photo Booth</p>
  <p class="service-copy" style="left:510px;top:345px;width:225px">Add more fun and excitement to your event with our photo booth. We offer several back drops and props!</p>

  <div class="photo photo-purple" style="left:505px;top:390px;width:230px;height:100px" role="img" aria-label="Photo of a lively dance floor at a wedding reception"></div>
  <p class="service-title" style="left:510px;top:499px">6. DJ Entertainment</p>
  <p class="service-copy" style="left:510px;top:514px;width:225px">All of our team members are highly trained professional Djs and emcees with their own unique style.</p>
</section>
<div class="side-label label-inside">INSIDE</div>

</body>
</html>
```